Brochure to advertise our unique physiotherapy clinic to general practitioners

We want to advertise our unique physiotherapy clinic to general practitioners (GPs) to develop there awareness of both our existence and services offered. The brochure should highlight our uniqueness (i.e. providing the highest quality care, advice and education) based on our expert research-based knowledge and skills. After reading the brochure, we want GPs to feel like they know us a little and feel happy to refer their patients to our clinic.
Attached is a draft flyer containing our logo, contact details, profile pictures and the information we would like to be contained in the brochure. We would like the brochure to be A4 double sided and able to be folded to fit into an envelope. More material (pictures) and understanding of our clinic can be found at www.kinetreva.com.au

A brief background of our team:
Our team currently consists of two physiotherapists specialising in the management of musculoskeletal and sports injuries, Dr Howard Tenniscombe and Dr Lionel Fairweather. Both Howard and Lionel have completed PhDs related to musculosketal injury management, and continue to be actively involved in international research groups. Between them they have authored more than 50 peer reviewed papers, presented at countless national and international conferences, and coordinate numerous courses to facilitate professional development of other clinicians. Most importantly, they continue to enjoy mixing these research and teaching activities with treating patients.

Updates
Project Deadline Extended
Reason: Consultation with clinic partner is needed and to allow time for modifications and additional designs. We will pick one, just want quality.
Thanks

Project Deadline Extended

Thank you for some great designs thus far everyone. We have decided to remove the fees from the brochure so please do the same for any future submissions. In the process of trying to provide feedback now.
Thanks
Project Deadline Extended
Reason: A couple of designs are close and we want to allow time to make appropriate modifications. This will be the last extension. Thanks for everyones effort so far

Project Deadline Extended

Target Market(s)
Australian General Practitioners and other health professionals are the targeted audience
Industry/Entity Type
Clinic
Look and feel

```html
<!DOCTYPE html>
<html lang="en">
<head>
<meta charset="utf-8">
<title>Kinetreva Clinic Brochure – Front and Back</title>
<link rel="stylesheet" href="https://fonts.googleapis.com/css2?family=PT+Sans:wght@400;700&family=Kaushan+Script&display=swap">
<style>
  :root {
    --canvas: #f2f2f2;
    --paper: #c49a6c;
    --band-blue: #1a7fbb;
    --band-yellow: #dfe24f;
    --ink: #1f1a14;
    --shadow: #000000;
    --footer-ink: #14202a;
    --mark-blue: #3f8fc4;
  }
  * { margin: 0; padding: 0; box-sizing: border-box; }
  html, body { width: 1200px; height: 1000px; overflow: hidden; }
  body {
    position: relative;
    background: var(--canvas);
    font-family: "PT Sans", Arial, sans-serif;
    color: var(--ink);
  }
  .sheet {
    position: absolute;
    background: var(--paper);
    box-shadow: 8px 12px 0 var(--shadow);
  }
  .sheet--front { left: 121px; top: 95px; width: 370px; height: 524px; }
  .sheet--back { left: 712px; top: 408px; width: 363px; height: 513px; }

  .top-band { position: absolute; left: 0; top: 0; width: 100%; height: 15px; display: flex; }
  .top-band span { flex: 1; background: var(--band-blue); }
  .top-band span.accent { background: var(--band-yellow); flex: 0.96; }

  .foot-band {
    position: absolute; left: 0; bottom: 0; width: 100%; height: 59px;
    background: var(--band-blue);
    text-align: center; font-size: 7.8px; line-height: 10.5px;
    color: var(--footer-ink); padding-top: 9px;
  }
  .foot-band .address { margin-bottom: 4px; }

  .brand {
    position: absolute; left: 78px; top: 44px;
    display: flex; align-items: center; gap: 10px;
    font-size: 26px; font-weight: 700; color: var(--mark-blue); letter-spacing: -0.5px;
  }
  .brand-dot { width: 32px; height: 32px; border-radius: 50%; background: var(--mark-blue); }

  .front-copy { position: absolute; left: 16px; top: 110px; width: 268px; }
  .front-copy h2 { font-weight: 400; font-size: 16.5px; line-height: 17px; }
  .front-copy p { font-size: 8.3px; line-height: 11.4px; margin-bottom: 8px; }

  .back-copy { position: absolute; left: 14px; top: 26px; width: 346px; font-size: 8.7px; line-height: 12.8px; }
  .back-copy .lead-strong { font-weight: 700; }
  .condition-list { list-style: none; margin-left: 4px; }
  .condition-list li::before { content: "•"; display: inline-block; width: 10px; }
  .condition-list .pair { word-spacing: 1px; }
  .fees { margin-top: 10px; }
  .fees h3 { font-size: 8.7px; font-weight: 700; }
  .fees p { margin-left: 4px; }
  .fees p span { display: inline-block; width: 18px; }

  .faint-name {
    position: absolute; left: 78px; top: 200px;
    font-size: 27px; font-weight: 700; color: var(--mark-blue); opacity: 0.22;
    transform: rotate(-8deg); transform-origin: left center;
  }

  .clinician-photo {
    position: absolute; left: 222px; top: 343px; width: 133px; height: 100px;
    background: linear-gradient(135deg, #e8e9ee 0%, #9aa6c0 50%, #4b4f62 100%);
  }

  .side-label {
    position: absolute; font-family: "Kaushan Script", cursive; font-size: 66px; color: #000; line-height: 1;
  }
  .side-label--back { left: 796px; top: 276px; }
  .side-label--front { left: 200px; top: 654px; }
</style>
</head>
<body>

  <section class="sheet sheet--front" aria-label="Brochure front">
    <div class="top-band"><span></span><span class="accent"></span><span></span></div>
    <div class="brand"><span class="brand-dot"></span>Kinetreva</div>

    <div class="front-copy">
      <h2>The Clinic</h2>
      <p>We are a very unique and progressive physiotherapy clinic at Kinetreva. Our clinic is located within Summit Fitness, Level 4, 21-22, Larkin Avenue, Ashbourne East, VIC, 3199. Further information about us is detailed below. Additionally, please visit our website and join the associated ‘tendinopathy’ ‘patellofemoral’ and ‘biomechanics’ blogs if you are interested at: http://www.kinetreva.com.au/</p>
      <h2>Who are we?</h2>
      <p>Our team currently consists of two physiotherapists specialising in the management of musculoskeletal and sports injuries, Dr Howard Tenniscombe and Dr Lionel Fairweather. Both Howard and Lionel have completed PhDs related to musculosketal injury management, and continue to be actively involved in international research groups. Between them they have authored more than 40 peer reviewed papers, presented at countless national and international conferences, and coordinate numerous courses to facilitate professional development of other clinicians. Most importantly, they continue to enjoy mixing these research and teaching activities with treating patients.</p>
      <h2>Services offered</h2>
      <p>All patients receive the highest quality 1-1 physiotherapy treatment and we offer patients accurate, realistic and lasting solution to their problems. We can guarantee the quality of our treatment because we are genuine experts in managing difficult injuries, with a wealth of clinical and research experience. This ultimately means we can more effective care, saving patients both time and money.</p>
    </div>

    <footer class="foot-band">
      <p class="address">c/o Summit Fitness, Level 4, The Courtyard,21-22 Larkin Ave, Ashbourne, 3198</p>
      <p>info@kinetreva.com.au</p>
      <p>www.kinetreva.com.au</p>
      <p>9000 4417</p>
    </footer>
  </section>

  <section class="sheet sheet--back" aria-label="Brochure back">
    <div class="top-band"><span></span><span class="accent"></span><span></span></div>
    <div class="faint-name" aria-hidden="true">Kinetreva</div>

    <div class="back-copy">
      <p>We have the facilities, knowledge and skills to complete comprehensive biomechanical assessments, evidence based exercise prescription, access to a full gym, highly effective manual therapy techniques, dry needling, diagnostic ultrasound, shockwave therapy, and foot orthoses advice/prescription.</p>
      <p>Put together, this will ensure all patients who attend our clinic an optimal recovery from almost any musculoskeletal injury, whether acute or chronic.</p>
      <p>We treat injuries others cannot fix</p>
      <p class="lead-strong">We have a reputation for successfully managing injuries that are difficult, or unresolving, including:</p>
      <ul class="condition-list">
        <li>Achilles tendinopathy</li>
        <li>Patellar tendinopathy</li>
        <li>Tennis elbow</li>
        <li>Rotator cuff injury</li>
        <li>Hamstring origin tendinopathy</li>
        <li>Tibialis posterior tendon injury</li>
        <li>Plantar fasciitis</li>
        <li class="pair">Iliotibial band syndrome &nbsp;&nbsp; • &nbsp;&nbsp;Patellofemoral joint injury</li>
        <li>Back and neck pain</li>
        <li>Chronic strains and sprains</li>
        <li>Shoulder pain</li>
        <li>Groin pain</li>
        <li>Hip impingement</li>
        <li>Stress fractures</li>
        <li>Shin splints (exercise induced leg pain)</li>
      </ul>
      <div class="fees">
        <h3>Fees:</h3>
        <p><span>-</span>All treatment sessions are 30 minutes</p>
      </div>
    </div>

    <div class="clinician-photo" role="img" aria-label="Photo of a physiotherapist at a diagnostic ultrasound machine in the clinic"></div>

    <footer class="foot-band">
      <p class="address">c/o Summit Fitness, Level 4, The Courtyard,21-22 Larkin Ave, Ashbourne, 3198</p>
      <p>info@kinetreva.com.au</p>
      <p>www.kinetreva.com.au</p>
      <p>9000 4417</p>
    </footer>
  </section>

  <div class="side-label side-label--back">Back</div>
  <div class="side-label side-label--front">Front</div>

</body>
</html>
```